Business card design needed

A earthmoving company, in the background would be good if there could be a picture of a (scraper), we have a business card already with lumo stack you may be able to see that?

Industry/Entity Type

Business

Contact Information for Business Card

Company name: Brindle Earthmoving

Corwin Brindle
514 Tarrabin-Keswell Rd
Mount Carrow
4815
0491 736 052
corwin_brindle@mailbrook.net

on the rear of the card
Equipment Hire and Contract

All Earthmoving, Mining and Civil Contruction

```html
<!DOCTYPE html>
<html lang="en">
<head>
<meta charset="utf-8">
<title>Brindle Earthmoving – Business Card</title>
<link rel="stylesheet" href="https://fonts.googleapis.com/css2?family=Montserrat:wght@600&family=Open+Sans:wght@400&display=swap">
<style>
  :root {
    --navy: #0b1a6f;
    --paper: #ffffff;
    --ink: #1a1a1a;
    --accent: #f07a12;
    --backdrop: #ece7dd;
    --art-light: #3f63c4;
    --art-mid: #1d3a9a;
    --art-warm: #c9803a;
  }
  * { box-sizing: border-box; margin: 0; padding: 0; }
  html, body {
    width: 1176px;
    height: 1200px;
    overflow: hidden;
    background: var(--backdrop);
  }
  .canvas {
    position: relative;
    width: 1176px;
    height: 1200px;
  }
  .card {
    position: absolute;
    background: var(--paper);
    box-shadow: 0 2px 6px rgba(0,0,0,0.18);
  }

  /* Front */
  .card-front {
    left: 94px;
    top: 105px;
    width: 848px;
    height: 466px;
    padding: 9px;
  }
  .front-panel {
    position: relative;
    width: 100%;
    height: 100%;
    background: var(--navy);
    color: var(--paper);
    font-family: "Open Sans", Arial, sans-serif;
  }
  .hero-art {
    position: absolute;
    left: 42px;
    top: 112px;
    width: 334px;
    height: 290px;
    background: linear-gradient(135deg, var(--art-light) 0%, var(--art-mid) 55%, var(--art-warm) 100%);
  }
  .owner-name {
    position: absolute;
    left: 400px;
    top: 40px;
    font-family: "Montserrat", Arial, sans-serif;
    font-weight: 600;
    font-size: 27px;
    line-height: 32px;
  }
  .company-name {
    position: absolute;
    left: 400px;
    top: 112px;
    font-family: "Montserrat", Arial, sans-serif;
    font-weight: 600;
    font-size: 40px;
    line-height: 44px;
    color: var(--accent);
  }
  .contact {
    position: absolute;
    left: 400px;
    top: 250px;
    list-style: none;
    font-size: 26px;
    line-height: 35px;
  }

  /* Back */
  .card-back {
    left: 243px;
    top: 664px;
    width: 834px;
    height: 447px;
    padding: 10px 10px 14px;
    display: flex;
    flex-direction: column;
  }
  .band {
    width: 100%;
    height: 115px;
    background: var(--navy);
  }
  .services {
    flex: 1;
    display: flex;
    flex-direction: column;
    align-items: center;
    justify-content: center;
    font-family: "Open Sans", Arial, sans-serif;
    font-size: 25px;
    line-height: 34px;
    color: var(--ink);
    text-align: center;
  }
</style>
</head>
<body>
<main class="canvas">

  <section class="card card-front" aria-label="Business card front">
    <div class="front-panel">
      <div class="hero-art" role="img" aria-label="Orange excavators on a blue engineering blueprint"></div>
      <p class="owner-name">Corwin Brindle</p>
      <p class="company-name">Brindle<br>Earthmoving</p>
      <ul class="contact">
        <li>514 Tarrabin-Keswell Rd</li>
        <li>Mount Carrow 4815</li>
        <li>T: 0491 736 052</li>
        <li>E: corwin_brindle@mailbrook.net</li>
      </ul>
    </div>
  </section>

  <section class="card card-back" aria-label="Business card back">
    <div class="band band-top"></div>
    <div class="services">
      <p>Equipment Hire and Contract</p>
      <p>All Earthmoving, Mining and Civil Contruction</p>
    </div>
    <div class="band band-bottom"></div>
  </section>

</main>
</body>
</html>
```